Business Card Design

we are a brand new cable TV network devoted to self improvement and leading a better life called FLOURIVO TV.I have a logo. We have 3 executives that need cards.I want it to be a heavy stock card: professional but showing our creative nature

Industry/Entity Type

Business

Contact Information for Business Card

CLAUDIA SAENZ AMLIECEO350 San Juan DrPonte Vedra Beach FL 32082904-473-5953

```html
<!DOCTYPE html>
<html lang="en">
<head>
<meta charset="utf-8">
<title>FLOURIVO TV — Business Card</title>
<link href="https://fonts.googleapis.com/css2?family=Lato:wght@300;400;700;900&display=swap" rel="stylesheet">
<style>
  :root {
    --backdrop: #5a605e;
    --card: #ffffff;
    --brand-red: #d2161e;
    --band-black: #1f1f21;
    --ink: #1c1c1c;
    --muted: #6f6f6f;
    --mark-tint: #f1d6cc;
  }
  html, body {
    margin: 0;
    width: 1200px;
    height: 1200px;
    overflow: hidden;
    background: var(--backdrop);
    font-family: "Lato", sans-serif;
  }
  .card {
    position: absolute;
    left: 100px;
    top: 314px;
    width: 1000px;
    height: 572px;
    background: var(--card);
    border-radius: 48px;
    overflow: hidden;
  }
  .brand-mark-area {
    position: absolute;
    left: 640px;
    top: 0;
    width: 330px;
    height: 440px;
    border-radius: 0 0 40px 40px;
    background: linear-gradient(180deg, var(--mark-tint) 0%, rgba(241,214,204,0.35) 100%);
  }
  .wordmark {
    position: absolute;
    left: 70px;
    top: 70px;
    font-weight: 900;
    font-size: 60px;
    letter-spacing: -1px;
    color: var(--ink);
  }
  .holder {
    position: absolute;
    right: 90px;
    top: 204px;
    text-align: right;
  }
  .holder-name {
    font-size: 30px;
    line-height: 36px;
    color: var(--brand-red);
    font-weight: 400;
  }
  .holder-name strong { font-weight: 900; }
  .holder-title {
    font-size: 22px;
    line-height: 26px;
    color: var(--muted);
    font-weight: 300;
    margin-top: 4px;
  }
  .divider {
    position: absolute;
    left: 130px;
    right: 152px;
    top: 246px;
    height: 2px;
    background: var(--brand-red);
  }
  .contact {
    position: absolute;
    left: 130px;
    top: 320px;
    font-size: 26px;
    color: var(--muted);
    line-height: 1.25;
  }
  .contact-row {
    display: flex;
    align-items: flex-start;
    gap: 18px;
    margin-bottom: 16px;
  }
  .contact-row svg { flex: none; margin-top: 4px; }
  .contact strong { font-weight: 900; }
  .bottom-bands {
    position: absolute;
    left: 0;
    bottom: 0;
    width: 1000px;
    height: 140px;
  }
  .band-label {
    position: absolute;
    right: 90px;
    bottom: 40px;
    color: #ffffff;
    font-size: 32px;
    font-weight: 400;
    letter-spacing: 1px;
  }
</style>
</head>
<body>
  <div class="card">
    <div class="brand-mark-area" role="img" aria-label="Faint oversized brand mark decoration"></div>

    <div class="wordmark">FLOURIVO TV</div>

    <div class="holder">
      <div class="holder-name"><strong>Mirella</strong> Okafor Dunst</div>
      <div class="holder-title">CEO</div>
    </div>
    <div class="divider"></div>

    <div class="contact">
      <div class="contact-row">
        <svg width="26" height="22" viewBox="0 0 26 22" aria-hidden="true">
          <path d="M2 7 Q13 -2 24 7 L21 10 L17 8 L17 5 Q13 3 9 5 L9 8 L5 10 Z" fill="#d2161e"/>
          <rect x="5" y="11" width="16" height="10" rx="2" fill="#d2161e"/>
        </svg>
        <span>904-618-2047</span>
      </div>
      <div class="contact-row">
        <svg width="26" height="30" viewBox="0 0 26 30" aria-hidden="true">
          <path d="M13 2 A9 9 0 0 1 22 11 C22 18 13 28 13 28 C13 28 4 18 4 11 A9 9 0 0 1 13 2 Z" fill="#d2161e"/>
          <circle cx="13" cy="11" r="3.5" fill="#ffffff"/>
        </svg>
        <span><strong>718</strong> Harlow Creek Dr<br>Ponte Vedra Beach FL 32097</span>
      </div>
    </div>

    <svg class="bottom-bands" viewBox="0 0 1000 140" aria-hidden="true">
      <path d="M0 88 H600 Q622 88 628 66 L634 40 Q640 18 668 18 H1000 V140 H0 Z" fill="var(--brand-red)"/>
      <path d="M640 40 Q646 8 680 8 H1000 V140 H0 V126 H610 Q628 126 632 100 Z" fill="var(--band-black)"/>
    </svg>
    <div class="band-label">FLOURIVO TV</div>
  </div>
</body>
</html>
```